perch 17 design

We are needing a website built for our company. We are based in the Dallas/Ft. Worth area providing staging for realtors, occupied staging, apartments, builders and hospitality industry ( Kip Nests .) Have been in the design and furniture industry for 35+ years, looking to expand our services to the area. Here Are some of the buzzword used for staging. Turn properties into dream spaces. Staging preparing property for sale.
Design services offered for new construction . We want to incorporate our tag line Turning you property into a dream Space .
Industry/Entity Type
interior and home design
Coding
Coded - Design and coding required
Number of Pages Required
2 page

```html
<!DOCTYPE html>
<html lang="en">
<head>
<meta charset="utf-8">
<title>Perch 17 Design — Home Staging</title>
<link href="https://fonts.googleapis.com/css2?family=Poppins:wght@400;500;600;700;800&display=swap" rel="stylesheet">
<style>
:root{
  --blue:#0a6fbe;
  --blue-dark:#075a9c;
  --ink:#111111;
  --text:#444444;
  --muted:#666666;
  --light:#f2f2f2;
  --white:#ffffff;
}
*{margin:0;padding:0;box-sizing:border-box}
html,body{width:1200px;height:5333px;overflow:hidden}
body{font-family:'Poppins',sans-serif;color:var(--text);background:var(--white);position:relative}
section,header,footer{position:absolute;left:0;width:1200px}

/* header */
.site-header{top:0;height:139px;background:var(--white)}
.topbar{position:absolute;right:0;top:0;width:538px;height:46px;background:var(--blue);clip-path:polygon(34px 0,100% 0,100% 100%,0 100%);display:flex;align-items:center;padding-left:50px;gap:12px;color:var(--white);font-size:14px;font-weight:600;letter-spacing:.5px}
.social-dot{width:11px;height:11px;border-radius:50%;background:var(--white);display:inline-block}
.topbar .call{margin-left:18px;display:flex;align-items:center;gap:8px}
.brand{position:absolute;display:flex;align-items:center;gap:9px;color:var(--ink);font-weight:700;white-space:nowrap;line-height:1}
.brand .mark{background:var(--ink);flex:0 0 auto}
.site-header .brand{left:114px;top:46px;font-size:22px}
.site-header .brand .mark{width:13px;height:13px}
.main-nav{position:absolute;top:86px;left:0;width:1200px;font-size:14px;font-weight:600;color:var(--ink);letter-spacing:.8px}
.main-nav a{position:absolute;transform:translateX(-50%);text-decoration:none;color:inherit;white-space:nowrap}
.main-nav a.active::after{content:"";position:absolute;left:50%;transform:translateX(-50%);bottom:-14px;width:44px;height:4px;background:var(--ink)}

/* hero */
.hero{top:139px;height:664px;background:linear-gradient(90deg,#080808 0%,#2c2824 30%,#8f8577 55%,#c9c2b6 80%,#d8d3ca 100%)}
.hero h1{position:absolute;left:143px;top:250px;font-size:47px;font-weight:700;color:var(--white);line-height:1.2;letter-spacing:.5px;text-transform:uppercase}
.dots{position:absolute;top:614px;left:546px;display:flex;gap:14px}
.dots span{width:11px;height:11px;border-radius:50%;background:var(--white)}
.dots span:first-child{background:transparent;border:2px solid var(--white)}

/* services band */
.services{top:803px;height:343px;background:var(--blue);color:var(--white)}
.services h2{position:absolute;top:58px;width:100%;text-align:center;font-size:28px;font-weight:600}
.svc{position:absolute;top:148px;width:180px;transform:translateX(-50%);text-align:center;font-size:20px;line-height:1.05}
.svc svg{display:block;margin:0 auto 20px;width:72px;height:72px}
.divider{position:absolute;top:150px;width:2px;height:128px;background:rgba(255,255,255,.55)}

/* about */
.about{top:1146px;height:747px}
.about h2{position:absolute;left:128px;top:174px;font-size:50px;font-weight:700;color:var(--ink);letter-spacing:1px}
.about p{position:absolute;left:128px;top:265px;width:400px;font-size:14px;line-height:20.5px;color:var(--muted)}
.btn-blue{position:absolute;background:var(--blue);color:var(--white);font-size:13px;font-weight:600;letter-spacing:1px;display:flex;align-items:center;justify-content:center;gap:8px}
.about .btn-blue{left:128px;top:470px;width:145px;height:41px}
.about .photo{position:absolute;left:581px;top:122px;width:491px;height:453px;background:radial-gradient(circle at 70% 55%,#4f7a3e 0%,#8c9a7c 25%,#b4aea4 55%,#5b4a40 100%)}
.badge{position:absolute;left:505px;top:459px;width:157px;height:158px;background:var(--white);box-shadow:0 6px 24px rgba(0,0,0,.15);text-align:center;color:var(--ink)}
.badge .num{display:block;font-size:54px;font-weight:800;margin-top:24px;line-height:1;letter-spacing:-1px}
.badge .yrs{display:block;font-size:26px;font-weight:600;letter-spacing:2px;margin-top:6px}

/* turn properties */
.turn{top:1893px;height:571px;background:linear-gradient(90deg,#c9c1b4 0%,#ddd7cd 30%,#ebe8e3 55%,#f2f1ef 100%)}
.turn h2{position:absolute;left:641px;top:136px;font-size:34px;font-weight:600;color:var(--ink);line-height:39px;letter-spacing:1.5px}
.turn p{position:absolute;left:641px;top:242px;width:470px;font-size:14px;line-height:20.5px;color:var(--muted)}
.turn .link{position:absolute;left:668px;top:428px;font-size:14px;font-weight:600;color:var(--ink);letter-spacing:1px}

/* staging for sale */
.staging{top:2464px;height:646px;background:linear-gradient(180deg,#1e1e1e,#2d2d2d 50%,#1b1b1b)}
.staging h2{position:absolute;top:108px;width:100%;text-align:center;font-size:34px;font-weight:600;color:var(--white);letter-spacing:1.5px}
.card{position:absolute;top:195px;width:298px;height:356px;background:var(--white);text-align:center}
.card .thumb{position:absolute;left:10px;top:10px;width:278px;height:199px}
.card p{position:absolute;top:242px;width:100%;font-size:14px;font-weight:600;color:var(--ink);line-height:21px}
.card .btn-line{position:absolute;left:50%;transform:translateX(-50%);top:294px;width:108px;height:35px;border:2px solid var(--ink);font-size:13px;font-weight:600;color:var(--ink);line-height:31px;letter-spacing:.5px}

/* design services */
.design{top:3110px;height:604px}
.design .photo{position:absolute;left:128px;top:105px;width:377px;height:397px;background:linear-gradient(160deg,#c4a888 0%,#e8e0d4 40%,#6a5a4a 70%,#2d2622 100%)}
.design h2{position:absolute;left:577px;top:159px;font-size:30px;font-weight:500;color:var(--ink);line-height:38px;letter-spacing:.5px}
.design p{position:absolute;left:579px;top:250px;width:490px;font-size:14px;line-height:20px;color:var(--muted)}
.design .btn-blue{left:579px;top:339px;width:203px;height:41px}

/* gallery */
.gallery{top:3714px;height:590px;background:var(--light)}
.gallery h2{position:absolute;top:44px;width:100%;text-align:center;font-size:48px;font-weight:700;color:var(--ink);letter-spacing:1px}
.tile{position:absolute;border:6px solid var(--white)}

/* quote */
.quote{top:4304px;height:589px;background:linear-gradient(180deg,var(--blue) 0%,var(--blue) 45%,var(--blue-dark) 100%)}
.quote h2{position:absolute;top:102px;width:100%;text-align:center;font-size:36px;font-weight:700;color:var(--white);letter-spacing:1px}
.quote .sub{position:absolute;top:159px;width:100%;text-align:center;font-size:14px;line-height:21px;color:var(--white)}
.field{position:absolute;background:var(--white);font-size:13px;color:var(--text);padding:10px 12px}
.submit{position:absolute;left:532px;top:467px;width:120px;height:39px;background:var(--ink);color:var(--white);font-size:15px;font-weight:600;letter-spacing:.5px;display:flex;align-items:center;justify-content:center}

/* footer */
.site-footer{top:4893px;height:440px;background:var(--light)}
.site-footer .brand{left:128px;top:150px;font-size:26px}
.site-footer .brand .mark{width:15px;height:15px}
.foot-col{position:absolute;top:98px}
.foot-col h3{font-size:19px;font-weight:500;color:var(--ink);letter-spacing:2px;margin-bottom:12px}
.foot-col li{list-style:none;font-size:14px;line-height:25px;color:var(--muted)}
.contact-item{display:flex;gap:14px;margin-bottom:16px;font-size:14px;line-height:18px;color:var(--muted)}
.contact-item .ic{flex:0 0 30px;width:30px;height:30px;border-radius:50%;background:var(--ink);display:flex;align-items:center;justify-content:center}
.foot-social{position:absolute;left:128px;top:378px;display:flex;gap:26px}
.foot-social span{width:20px;height:20px;border-radius:50%;background:var(--ink)}
.copy{position:absolute;right:124px;top:380px;font-size:14px;color:var(--muted)}
</style>
</head>
<body>

<header class="site-header">
  <div class="topbar">
    <span class="social-dot"></span><span class="social-dot"></span><span class="social-dot"></span><span class="social-dot"></span><span class="social-dot"></span>
    <span class="call">
      <svg width="15" height="15" viewBox="0 0 24 24" fill="#fff"><path d="M6.6 10.8a15 15 0 0 0 6.6 6.6l2.2-2.2a1 1 0 0 1 1-.25 11.4 11.4 0 0 0 3.6.6 1 1 0 0 1 1 1V20a1 1 0 0 1-1 1A17 17 0 0 1 3 4a1 1 0 0 1 1-1h3.5a1 1 0 0 1 1 1c0 1.25.2 2.45.6 3.6a1 1 0 0 1-.25 1z"/></svg>
      CALL US: 041 555 0193
    </span>
  </div>
  <div class="brand"><span class="mark"></span><span>Perch 17 Design</span></div>
  <nav class="main-nav">
    <a class="active" style="left:372px">HOME</a>
    <a style="left:513px">OUR SERVICES</a>
    <a style="left:650px">SALE</a>
    <a style="left:759px">DESIGN</a>
    <a style="left:888px">GALLERY</a>
    <a style="left:1028px">CONTACT</a>
  </nav>
</header>

<section class="hero" role="img" aria-label="Bright staged living room with sofa, armchair and tall windows">
  <h1>Turning you property<br>into a dream space</h1>
  <div class="dots"><span></span><span></span><span></span><span></span><span></span></div>
</section>

<section class="services">
  <h2>We Area Providing Staging for...</h2>
  <div class="svc" style="left:174px">
    <svg viewBox="0 0 64 64" fill="none" stroke="#fff" stroke-width="2.5"><path d="M8 32 32 10l24 22"/><path d="M14 28v26h36V28"/><rect x="27" y="38" width="10" height="16"/></svg>
    Realtors</div>
  <div class="divider" style="left:271px"></div>
  <div class="svc" style="left:375px">
    <svg viewBox="0 0 64 64" fill="none" stroke="#fff" stroke-width="2.5"><rect x="18" y="6" width="28" height="20"/><path d="M10 50V36a5 5 0 0 1 10 0v6h24v-6a5 5 0 0 1 10 0v14z"/><path d="M14 50v6M50 50v6"/></svg>
    Occupied<br>Staging</div>
  <div class="divider" style="left:480px"></div>
  <div class="svc" style="left:596px">
    <svg viewBox="0 0 64 64" fill="none" stroke="#fff" stroke-width="2.5"><rect x="10" y="8" width="28" height="50"/><rect x="38" y="22" width="18" height="36"/><path d="M16 16h6M26 16h6M16 26h6M26 26h6M16 36h6M26 36h6M44 30h6M44 40h6M20 58v-10h8v10"/></svg>
    Apartments</div>
  <div class="divider" style="left:706px"></div>
  <div class="svc" style="left:819px">
    <svg viewBox="0 0 64 64" fill="none" stroke="#fff" stroke-width="2.5"><path d="M14 28a18 18 0 0 1 36 0z"/><path d="M10 28h44M32 6v4"/><path d="M8 56V38h48v18M8 46h48"/></svg>
    Hospitality<br>Industry</div>
  <div class="divider" style="left:927px"></div>
  <div class="svc" style="left:1026px">
    <svg viewBox="0 0 64 64" fill="none" stroke="#fff" stroke-width="2.5"><path d="M14 30a18 18 0 0 1 36 0"/><path d="M10 30h44v6H10z"/><path d="M28 12h8v10h-8z"/><path d="M12 58c2-10 10-14 20-14s18 4 20 14"/></svg>
    Builders</div>
</section>

<section class="about">
  <h2>ABOUT US</h2>
  <p>Sed ut perspiciatis unde omnis iste natus error sit voluptatem accusantium doloremque laudantium, totam rem aperiam, eaque ipsa quaeae ab illo inventore veritatis et quasi architecto beatae vitae dicta sunt explicabo. Nemo enim ipsam voluptatem quia voluptas sit aspernatur aut odit aut fugit, sed quia consequuntur magni dolores eos qui ratione voluptatem sequi nesciunt.</p>
  <div class="btn-blue">READ MORE</div>
  <div class="photo" role="img" aria-label="Console table styled with a leafy plant, glass vase and coral decor"></div>
  <div class="badge"><span class="num">35+</span><span class="yrs">YEARS</span></div>
</section>

<section class="turn" role="img" aria-label="Staged living room with white sofas, fireplace and ceiling fan">
  <h2>TURN PROPERTIES<br>INTO DREAM SPACES.</h2>
  <p>Sed ut perspiciatis unde omnis iste natus error sit voluptate m accusantium doloremque laudantium, totam rem aperiam, eaque ipsa quaeae ab illo inventore veritatis et quasi architecto beatae vitae dicta sunt explicabo. Nemo enim ipsam voluptatem quia voluptas sit aspernatur aut odit aut fugit, sed quia consequuntur magni dolores eos qui ratione voluptatem sequi nesciunt.</p>
  <div class="link">VIEW OUR PORTFOLIO</div>
</section>

<section class="staging">
  <h2>STAGING PREPARING PROPERTY FOR SALE</h2>
  <div class="card" style="left:126px">
    <div class="thumb" role="img" aria-label="Staged bedroom with tufted headboard" style="background:linear-gradient(180deg,#d9d6d0,#a9a49c 60%,#3a3a3a)"></div>
    <p>Sed ut perspiciatis unde<br>om iste natus erloremror sit.</p>
    <div class="btn-line">SALE NOW</div>
  </div>
  <div class="card" style="left:449px">
    <div class="thumb" role="img" aria-label="Staged living room with white sofas" style="background:linear-gradient(180deg,#e4e3e0,#cfccc6 60%,#9b958c)"></div>
    <p>Sed ut perspiciatis unde<br>om iste natus erloremror sit.</p>
    <div class="btn-line">SALE NOW</div>
  </div>
  <div class="card" style="left:772px">
    <div class="thumb" role="img" aria-label="Staged home office with desk and rug" style="background:linear-gradient(180deg,#dcdad6,#c2bfb8 60%,#8e8a84)"></div>
    <p>Sed ut perspiciatis unde<br>om iste natus erloremror sit.</p>
    <div class="btn-line">SALE NOW</div>
  </div>
</section>

<section class="design">
  <div class="photo" role="img" aria-label="Reading corner with leather armchairs and round side table"></div>
  <h2>DESIGN SERVICES OFFERED FOR<br>NEW CONSTRUCTION.</h2>
  <p>Lorem ipsum dolor sit amet, consectetur adipiscing elit, sed do eiusmod tempor incididunt ut labore et dolore magna aliqua. Quis ipsum suspendisse ultrices gravida.</p>
  <div class="btn-blue">
    <svg width="13" height="13" viewBox="0 0 24 24" fill="#fff"><path d="M6.6 10.8a15 15 0 0 0 6.6 6.6l2.2-2.2a1 1 0 0 1 1-.25 11.4 11.4 0 0 0 3.6.6 1 1 0 0 1 1 1V20a1 1 0 0 1-1 1A17 17 0 0 1 3 4a1 1 0 0 1 1-1h3.5a1 1 0 0 1 1 1c0 1.25.2 2.45.6 3.6a1 1 0 0 1-.25 1z"/></svg>
    RECEIVE A QUOTE</div>
</section>

<section class="gallery">
  <h2>OUR GALLERY</h2>
  <div class="tile" role="img" aria-label="Bedroom with white bedding" style="left:124px;top:155px;width:302px;height:151px;background:linear-gradient(180deg,#d7d6d2,#bdbab4)"></div>
  <div class="tile" role="img" aria-label="Bedroom with artwork above the bed" style="left:124px;top:302px;width:302px;height:192px;background:linear-gradient(180deg,#e2ded8,#c9c1b6)"></div>
  <div class="tile" role="img" aria-label="Kids room with wooden bed" style="left:449px;top:155px;width:302px;height:143px;background:linear-gradient(180deg,#8d7b6a,#d8d2ca)"></div>
  <div class="tile" role="img" aria-label="Bunk bedroom with navy wall" style="left:449px;top:294px;width:302px;height:200px;background:linear-gradient(180deg,#3a4a66,#b7aea5)"></div>
  <div class="tile" role="img" aria-label="Living room with sofa and windows" style="left:774px;top:155px;width:157px;height:339px;background:linear-gradient(180deg,#d6d5d2,#a09c98)"></div>
  <div class="tile" role="img" aria-label="Corner with plant and white stools" style="left:927px;top:155px;width:151px;height:339px;background:linear-gradient(180deg,#d9d9d6,#7d8a6a 50%,#d4d1cb)"></div>
</section>

<section class="quote" role="img" aria-label="Soft blue-tinted bedroom backdrop">
  <h2>GET A QUOTE</h2>
  <p class="sub">Sed ut perspiciatis unde omnis iste natus error sit voluptate<br>m accusantium doloremque laudantium, totam.</p>
  <div class="field" style="left:333px;top:233px;width:253px;height:42px">First Name:</div>
  <div class="field" style="left:596px;top:233px;width:269px;height:42px">Last Name:</div>
  <div class="field" style="left:333px;top:289px;width:253px;height:42px">Phone:</div>
  <div class="field" style="left:596px;top:289px;width:269px;height:42px">Email:</div>
  <div class="field" style="left:333px;top:343px;width:532px;height:143px">Message:</div>
  <div class="submit">SUBMIT</div>
</section>

<footer class="site-footer">
  <div class="brand"><span class="mark"></span><span>Perch 17 Design</span></div>
  <div class="foot-col" style="left:408px">
    <h3>MENU</h3>
    <ul><li>Home</li><li>Our Services</li><li>Sale</li><li>Design</li><li>Gallery</li><li>Contact</li></ul>
  </div>
  <div class="foot-col" style="left:584px">
    <h3>LINKS</h3>
    <ul><li>Realtors</li><li>Occupied staging</li><li>Apartments</li><li>Builders</li><li>Hospitality industry</li></ul>
  </div>
  <div class="foot-col" style="left:815px;width:260px">
    <h3>CONTACT</h3>
    <div class="contact-item"><span class="ic"><svg width="14" height="14" viewBox="0 0 24 24" fill="#fff"><path d="M12 2a7 7 0 0 0-7 7c0 5 7 13 7 13s7-8 7-13a7 7 0 0 0-7-7zm0 9.5A2.5 2.5 0 1 1 12 6.5a2.5 2.5 0 0 1 0 5z"/></svg></span><span>Lorem Dum street 123 LJD<br>dumy numers 463.</span></div>
    <div class="contact-item"><span class="ic"><svg width="13" height="13" viewBox="0 0 24 24" fill="#fff"><path d="M6.6 10.8a15 15 0 0 0 6.6 6.6l2.2-2.2a1 1 0 0 1 1-.25 11.4 11.4 0 0 0 3.6.6 1 1 0 0 1 1 1V20a1 1 0 0 1-1 1A17 17 0 0 1 3 4a1 1 0 0 1 1-1h3.5a1 1 0 0 1 1 1c0 1.25.2 2.45.6 3.6a1 1 0 0 1-.25 1z"/></svg></span><span>Phone:<br>123 456 7890</span></div>
    <div class="contact-item"><span class="ic"><svg width="14" height="14" viewBox="0 0 24 24" fill="#fff"><path d="M3 5h18v14H3zm2 2v.5l7 5 7-5V7z"/></svg></span><span>Email:<br>info@company.com</span></div>
  </div>
  <div class="foot-social" aria-label="Social links"><span></span><span></span><span></span><span></span><span></span></div>
  <div class="copy">© 2023 Perch 17 Design. All rights are reserved.</div>
</footer>

</body>
</html>
```